Tidewell show guide

I need to design a one page 7x10 pdf that will be printed. It will include our logo and the following text:

#1 Disaster Mitigation Lead Platform

We generated over 60 million in
revenue last year fo our contractors.

Leads types:
-Water Damage
-Fire Damage
-Mold Remediation
-Biohazard
-Plumbing
-Carpet Cleaning

Exclusive leads
No monthly fees
Only pay for valid leads

Stop by booth 527 to get to your cut!

Target Market(s)

Home service contractors

Colors
9bcb3b
0255a3

Requirements
Must have
• our logo and text
Should not have
• any clutter

```html
<!DOCTYPE html>
<html lang="en">
<head>
<meta charset="utf-8">
<title>Tidewell show guide</title>
<link rel="stylesheet" href="https://fonts.googleapis.com/css2?family=Arimo:wght@400;700&family=Roboto+Condensed:wght@700&display=swap">
<style>
  :root {
    --lime: #9bcb3b;
    --navy: #0255a3;
    --sea: #3f8a7a;
    --ink: #1a1a1a;
    --white: #ffffff;
    --frame: #6b6b6b;
  }
  * { box-sizing: border-box; margin: 0; padding: 0; }
  html, body { width: 1200px; height: 1000px; overflow: hidden; background: var(--white); }
  body { position: relative; font-family: "Arimo", Arial, sans-serif; }

  .show-guide {
    position: absolute; left: 348px; top: 140px; width: 505px; height: 720px;
    border: 1px solid var(--frame); background: var(--white); overflow: hidden;
  }
  .top-band { position: absolute; left: 0; top: 0; width: 100%; height: 60px; background: var(--lime); }

  .title-banner {
    position: absolute; left: 0; top: 60px; width: 100%; height: 102px;
    background: linear-gradient(90deg, #ffffff 0%, #6f9ccc 8%, var(--navy) 22%, var(--navy) 78%, #6f9ccc 92%, #ffffff 100%);
  }
  .rank-badge { position: absolute; left: 52px; top: 6px; width: 66px; height: 88px; }
  .title {
    position: absolute; left: 134px; top: 12px;
    font-family: "Roboto Condensed", "Arial Narrow", sans-serif; font-weight: 700;
    font-size: 34px; line-height: 41px; color: var(--white); letter-spacing: 0.3px;
    text-shadow: 1px 2px 3px rgba(0,0,0,0.45);
  }

  .body-panel {
    position: absolute; left: 0; top: 162px; width: 100%; height: 469px;
    background: linear-gradient(180deg, #8fc44a 0%, #62a86b 35%, var(--sea) 60%, var(--navy) 100%);
  }
  .headline {
    position: absolute; left: 0; top: 21px; width: 100%; text-align: center;
    font-weight: 700; font-size: 25px; line-height: 30px; color: var(--white);
    text-shadow: 1px 2px 3px rgba(0,0,0,0.35); white-space: nowrap;
  }
  .lead-types-label { position: absolute; left: 38px; top: 112px; font-weight: 700; font-size: 14px; color: var(--ink); }

  .lead-types { list-style: none; }
  .lead-type {
    position: absolute; display: flex; align-items: center; gap: 5px;
    font-weight: 700; font-size: 14.5px; color: var(--ink); white-space: nowrap;
  }
  .lead-icon { width: 56px; height: 56px; flex: none; filter: drop-shadow(2px 3px 2px rgba(0,0,0,0.4)); }

  .benefits { position: absolute; left: 38px; top: 360px; list-style: none; }
  .benefit {
    font-weight: 700; font-size: 20px; line-height: 29px; color: var(--white);
    display: flex; align-items: center; gap: 9px;
  }
  .benefit svg { width: 21px; height: 21px; }

  .footer { position: absolute; left: 0; top: 631px; width: 100%; height: 89px; background: var(--white); }
  .booth-call { position: absolute; left: 39px; top: 19px; font-weight: 700; font-size: 18px; line-height: 25px; color: var(--ink); }
  .brand-name {
    position: absolute; left: 240px; top: 31px; white-space: nowrap;
    font-family: "Arimo", Arial, sans-serif; font-weight: 700; font-size: 22px; color: var(--navy);
  }
</style>
</head>
<body>
<main class="show-guide">
  <div class="top-band"></div>

  <header class="title-banner">
    <svg class="rank-badge" viewBox="0 0 66 88" aria-hidden="true">
      <polygon points="16,50 6,80 16,74 24,84 30,56" fill="#9bcb3b"/>
      <polygon points="50,50 60,80 50,74 42,84 36,56" fill="#7fb22e"/>
      <g fill="#ffffff">
        <circle cx="33" cy="32" r="27"/>
        <g transform="translate(33 32)">
          <polygon points="0,-32 4,-26 -4,-26"/><polygon points="0,32 4,26 -4,26"/>
          <polygon points="-32,0 -26,4 -26,-4"/><polygon points="32,0 26,4 26,-4"/>
          <polygon points="22,-22 22,-15 15,-22"/><polygon points="-22,22 -22,15 -15,22"/>
          <polygon points="-22,-22 -15,-22 -22,-15"/><polygon points="22,22 15,22 22,15"/>
          <polygon points="12,-30 16,-24 8,-26"/><polygon points="-12,30 -16,24 -8,26"/>
          <polygon points="-12,-30 -8,-26 -16,-24"/><polygon points="12,30 8,26 16,24"/>
          <polygon points="30,12 24,16 26,8"/><polygon points="-30,-12 -24,-16 -26,-8"/>
          <polygon points="30,-12 26,-8 24,-16"/><polygon points="-30,12 -26,8 -24,16"/>
        </g>
      </g>
      <text x="33" y="43" text-anchor="middle" font-family="Roboto Condensed, Arial Narrow, sans-serif" font-weight="700" font-size="31" fill="#111">#1</text>
    </svg>
    <h1 class="title">DISASTER MITIGATION<br>LEAD PLATFORM</h1>
  </header>

  <section class="body-panel">
    <p class="headline">We generated over 60 million in<br>revenue last year for our contractors!</p>
    <p class="lead-types-label">Leads types:</p>

    <ul class="lead-types">
      <li class="lead-type" style="left:37px;top:142px">
        <svg class="lead-icon" viewBox="0 0 56 56" aria-hidden="true"><circle cx="28" cy="28" r="27" fill="#0255a3"/><path d="M28 12 C24 21 19 27 19 34 a9 9 0 0 0 18 0 C37 27 32 21 28 12Z" fill="#fff"/></svg>
        Water Damage
      </li>
      <li class="lead-type" style="left:37px;top:206px">
        <svg class="lead-icon" viewBox="0 0 56 56" aria-hidden="true"><circle cx="28" cy="28" r="27" fill="#0255a3"/><path d="M28 11 C30 18 38 22 38 32 a10 10 0 0 1 -20 0 C18 26 22 23 23 18 C25 22 26 24 27 25 C28 20 29 16 28 11Z M28 30 C26 33 24 35 24 38 a4 4 0 0 0 8 0 C32 35 30 33 28 30Z" fill="#fff" fill-rule="evenodd"/></svg>
        Fire Damage
      </li>
      <li class="lead-type" style="left:37px;top:269px">
        <svg class="lead-icon" viewBox="0 0 56 56" aria-hidden="true"><circle cx="28" cy="28" r="27" fill="#0255a3"/><circle cx="28" cy="28" r="18" fill="#c9d9ec"/></svg>
        Mold Remediation
      </li>
      <li class="lead-type" style="left:236px;top:142px">
        <svg class="lead-icon" viewBox="0 0 56 56" aria-hidden="true"><circle cx="28" cy="28" r="27" fill="#0255a3"/><g fill="none" stroke="#fff" stroke-width="3"><circle cx="28" cy="20" r="8"/><circle cx="20" cy="34" r="8"/><circle cx="36" cy="34" r="8"/><circle cx="28" cy="30" r="10"/></g><circle cx="28" cy="29" r="3" fill="#fff"/></svg>
        Biohazard
      </li>
      <li class="lead-type" style="left:236px;top:206px">
        <svg class="lead-icon" viewBox="0 0 56 56" aria-hidden="true"><circle cx="28" cy="28" r="27" fill="#0255a3"/><path d="M19 11 v8 a9 9 0 0 0 6 8 v18 h6 v-18 a9 9 0 0 0 6 -8 v-8 l-4 0 v8 h-10 v-8Z" fill="#fff"/></svg>
        Plumbing
      </li>
      <li class="lead-type" style="left:236px;top:269px">
        <svg class="lead-icon" viewBox="0 0 56 56" aria-hidden="true"><circle cx="28" cy="28" r="27" fill="#0255a3"/><path d="M12 30 L32 40 L44 32 L24 22Z" fill="#fff"/><path d="M30 28 L44 14" stroke="#fff" stroke-width="3"/></svg>
        Carpet Cleaning
      </li>
    </ul>

    <ul class="benefits">
      <li class="benefit"><svg viewBox="0 0 20 20" aria-hidden="true"><polygon points="10,1 12.4,7.3 19,7.3 13.7,11.3 15.6,18 10,14 4.4,18 6.3,11.3 1,7.3 7.6,7.3" fill="#fff"/></svg>Exclusive leads</li>
      <li class="benefit"><svg viewBox="0 0 20 20" aria-hidden="true"><polygon points="10,1 12.4,7.3 19,7.3 13.7,11.3 15.6,18 10,14 4.4,18 6.3,11.3 1,7.3 7.6,7.3" fill="#fff"/></svg>No monthly fees</li>
      <li class="benefit"><svg viewBox="0 0 20 20" aria-hidden="true"><polygon points="10,1 12.4,7.3 19,7.3 13.7,11.3 15.6,18 10,14 4.4,18 6.3,11.3 1,7.3 7.6,7.3" fill="#fff"/></svg>Only pay for valid leads</li>
    </ul>
  </section>

  <footer class="footer">
    <p class="booth-call">Stop by booth 527<br>to get to your cut!</p>
    <p class="brand-name">Northbeam Leads</p>
  </footer>
</main>
</body>
</html>
```